Letterhead to Prospective Clients

Create a letterhead (word & canva) that I will use to send letters to prospective clients and also include the Harbourline Estate Group Logo, My Contact Details and Interchangeable "Suburb". Use the same font and colour pallete

Maris Toppel | "Suburb" Specialist - Coralmere & Surrounds
Mobile: 0417 862 905
Email: MT@HarbourlineEstateGroup.com.au

```html
<!DOCTYPE html>
<html lang="en">
<head>
<meta charset="utf-8">
<title>Harbourline Estate Group – Letterhead</title>
<link href="https://fonts.googleapis.com/css2?family=Arimo:wght@400;700&family=Josefin+Sans:wght@300&family=Montserrat:wght@600&display=swap" rel="stylesheet">
<style>
  :root{
    --navy:#0b1a33;
    --tan:#d79e68;
    --ink:#333a44;
    --muted:#555b63;
    --rule:#9aa0a6;
    --paper:#ffffff;
    --backdrop:#e6e7e9;
  }
  html,body{margin:0;width:1200px;height:960px;overflow:hidden;background:var(--backdrop);}
  .letterhead{
    position:absolute;left:282px;top:30px;width:636px;height:900px;
    background:var(--paper);overflow:hidden;
    box-shadow:0 2px 10px rgba(0,0,0,.12);
    font-family:"Arimo",Arial,sans-serif;color:var(--ink);
  }
  .header-swoosh{position:absolute;left:0;top:0;width:636px;height:160px;}
  .brand-name{
    position:absolute;right:34px;top:58px;margin:0;
    font-family:"Josefin Sans",sans-serif;font-weight:300;
    font-size:21px;letter-spacing:2px;color:var(--navy);text-transform:uppercase;
  }
  .letter-body{position:absolute;left:104px;top:205px;width:440px;}
  .salutation{font-family:"Montserrat",sans-serif;font-weight:600;font-size:14px;color:var(--ink);margin:0 0 10px;}
  .letter-body p.para{font-size:10.5px;line-height:1.32;margin:0 0 14px;color:var(--muted);}
  .sign-off{position:absolute;left:124px;top:585px;margin:0;font-family:"Montserrat",sans-serif;font-weight:600;font-size:9px;color:var(--ink);}
  .signature{position:absolute;left:150px;top:608px;width:120px;height:40px;background:linear-gradient(90deg,#eceef1,#f6f7f8);border-radius:4px;}
  .contact-block{position:absolute;right:40px;bottom:40px;width:380px;text-align:right;font-size:11.5px;color:var(--muted);}
  .contact-block .role{margin:0 0 6px;}
  .contact-block .rule{height:1px;background:var(--rule);margin:0 0 6px;}
  .contact-block .details{display:flex;justify-content:flex-end;gap:22px;align-items:center;}
  .contact-block .item{display:flex;align-items:center;gap:6px;}
  .contact-block svg{width:10px;height:10px;}
</style>
</head>
<body>
<main class="letterhead">
  <svg class="header-swoosh" viewBox="0 0 636 160" aria-hidden="true">
    <path fill="var(--navy)" d="M0 0 H636 V10 C330 14 80 40 0 125 Z"/>
    <path fill="var(--tan)" d="M600 17 C320 24 80 52 0 134 L0 148 C82 68 320 31 600 17 Z"/>
  </svg>

  <h1 class="brand-name">Harbourline Estate Group</h1>

  <section class="letter-body">
    <p class="salutation">Dear Mr. Smith,</p>
    <p class="para">Lorem ipsum dolor sit amet, consectetuer adipiscing elit, sed diam nonummy nibh euismod tincidunt ut laoreet dolore magna aliquam erat volutpat. Ut wisi enim ad minim veniam, quis nostrud exerci tation ullamcorper suscipit lobortis nisl ut aliquip ex ea commodo consequat. Duis autem vel eum iriure dolor in hendrerit in vulputate velit esse molestie consequat, vel illum dolore eu feugiat</p>
    <p class="para">Rorem ipsum dolor sit amet, consectetuer adipiscing elit, sed diam nonummy nibh euismod tincidunt ut laoreet dolore magna aliquam erat volutpat. Ut wisi enim ad minim veniam, quis nostrud exerci tation ullamcorper suscipit lobortis nisl ut aliquip ex ea commodo consequat. Duis autem vel eum iriure dolor in hendrerit in vulputate velit esse molest</p>
    <p class="para">Dorem ipsum dolor sit amet, consectetuer adipiscing elit, sed diam nonummy nibh euismod tincidunt ut laoreet dolore magna aliquam erat volutpat. Ut wisi enim ad minim veniam, quis nostrud exerci tation ullamcorper suscipit lobortis nisl ut aliquip ex ea commodo consequat. Duis autem vel eum iriure dolor in hendrerit in suscipit lobortis nisl ut aliquip ex ea commodo consequat. Duis autem vel eum iriure dolor in hendrerit in vulputate velit esse molestie consequat, vel illum</p>
    <p class="para">Sorem ipsum dolor sit amet, consectetuer adipiscing elit, sed diam nonummy nibh euismod tincidunt ut laoreet dolore magna aliquam erat volutpat. Ut wisi enim ad minim veniam, quis nostrud exerci tation ullamcorper suscipit lobortis nisl ut aliquip ex ea commodo consequat. Duis autem vel eum iriure dolor in</p>
  </section>

  <p class="sign-off">Sincerely,</p>
  <div class="signature" role="img" aria-label="Handwritten signature"></div>

  <footer class="contact-block">
    <p class="role">Maris Toppel | "Suburb" Specialist | Coralmere &amp; Surrounds</p>
    <div class="rule"></div>
    <div class="details">
      <span class="item">
        <svg viewBox="0 0 10 10" aria-hidden="true"><path fill="var(--tan)" d="M2 0.5 L3.8 2.6 L2.8 3.6 C3.4 5 5 6.6 6.4 7.2 L7.4 6.2 L9.5 8 L8.2 9.5 C4.5 9.2 0.8 5.5 0.5 1.8 Z"/></svg>
        0417 862 905
      </span>
      <span class="item">
        <svg viewBox="0 0 10 10" aria-hidden="true"><rect x="0.5" y="2" width="9" height="6.5" fill="var(--tan)"/><path d="M0.5 2 L5 5.8 L9.5 2" fill="none" stroke="#fff" stroke-width="0.8"/></svg>
        MT@HarbourlineEstateGroup.com.au
      </span>
    </div>
  </footer>
</main>
</body>
</html>
```